Easy Marinade Labels for Butchery Store

Need a set of labels designed for a Butchery Shop. They will sit in the top left corner of the packets as a triangle (7cm each side). Easy because the only major requirement is the label name and some small text saying "Please ask in store to see spec sheet for ingredients". Extra points for finding a fun way to incorporate the logo and/or images of food (garlic bulbs, chilli, spices ect) to enhance the label. List of Marinade Names below: GarlicPepper Mint & RosemarySatayBBQChilli Plum & GingerSundried Tomato & BasilBuffaloHoney SoyHoi-SinPer PeriSpicy CajunTeriyakiBlack Bean Ive also attached the logo and an example of how the label might sit on a packet of meat. Thanks

Target Market(s)

Butchery Deli Shop Customers

Industry/Entity Type

Food Store

Font styles to use
Serif
Sans Serif
Decorative
Other font styles liked:
• Fun font that isn't a generic Quillbrenn Font?

Colors

Designer to choose colors to be used in the design.

Requirements
Must have
• Product Name
• Small text saying "Please ask in store to see spec sheet for ingredients"
Nice to have
• Photos of ingredients that would match that type of marinade - Chilli, Garlic, Spices.
• Tavo Crest Logo - not essential if it doesn't look good on the label / doesn't fit.

```html
<!DOCTYPE html>
<html lang="en">
<head>
<meta charset="utf-8">
<title>Tavo Crest Marinade Labels</title>
<link rel="stylesheet" href="https://fonts.googleapis.com/css2?family=Saira+Condensed:wght@600;700&family=Oswald:wght@300;400&display=swap">
<style>
  :root {
    --ink: #9a6716;
    --cream: #f8f5ee;
    --spec-ink: #4a3a22;
    --bg-edge: #c9cdd0;
    --bg-mid: #ffffff;
    --brand: #9a6716;
  }
  html, body {
    margin: 0;
    padding: 0;
    width: 1200px;
    height: 923px;
    overflow: hidden;
  }
  body {
    background: radial-gradient(ellipse at center, var(--bg-mid) 45%, var(--bg-edge) 100%);
    position: relative;
  }
  .label {
    position: absolute;
    width: 288px;
    height: 144px;
  }
  .label svg.frame {
    position: absolute;
    inset: 0;
    width: 288px;
    height: 144px;
  }
  .frame .outer { fill: url(#goldRim); }
  .frame .accent { fill: var(--accent); }
  .frame .inner { fill: var(--cream); }
  .art {
    position: absolute;
    left: 50%;
    top: 22px;
    width: 54px;
    height: 32px;
    transform: translateX(-50%);
    border-radius: 14px 14px 6px 6px;
    background: var(--art);
  }
  .brand, .marinated, .name, .spec {
    position: absolute;
    left: 50%;
    transform: translateX(-50%);
    text-align: center;
    white-space: nowrap;
    line-height: 1;
  }
  .brand {
    top: 58px;
    font-family: "Saira Condensed", "Arial Narrow", sans-serif;
    font-weight: 700;
    font-size: 14px;
    color: var(--brand);
    letter-spacing: 0.3px;
  }
  .marinated {
    top: 82px;
    font-family: "Saira Condensed", "Arial Narrow", sans-serif;
    font-weight: 600;
    font-size: 7px;
    letter-spacing: 2px;
    color: var(--ink);
  }
  .name {
    top: 93px;
    font-family: "Saira Condensed", "Arial Narrow", sans-serif;
    font-weight: 700;
    font-size: 22px;
    color: var(--ink);
    text-transform: uppercase;
    letter-spacing: 0.5px;
    max-width: 180px;
  }
  .name.two-line {
    top: 91px;
    font-size: 17px;
    line-height: 16px;
  }
  .spec {
    top: 123px;
    font-family: "Oswald", "Arial Narrow", sans-serif;
    font-weight: 300;
    font-size: 8px;
    color: var(--spec-ink);
  }
  .col-1 { left: 80px; }
  .col-2 { left: 455px; }
  .col-3 { left: 830px; }
  .row-1 { top: 28px; }
  .row-2 { top: 209px; }
  .row-3 { top: 390px; }
  .row-4 { top: 570px; }
  .row-5 { top: 752px; }

  .tomato   { --accent: #c8251c; --art: linear-gradient(#d9361f, #5e9a3a); }
  .garlic   { --accent: #a79a82; --art: linear-gradient(#f4eee0, #c9bca2); }
  .honey    { --accent: #d8c629; --art: linear-gradient(#ffd84a, #e6a818); }
  .peri     { --accent: #d0301c; --art: linear-gradient(#d4261a, #e8e2d2); }
  .bean     { --accent: #2f7a3a; --art: linear-gradient(#3a3a3a, #111111); }
  .hoisin   { --accent: #e8c51c; --art: linear-gradient(#de2910, #c81e0c); }
  .pepper   { --accent: #2d2d2d; --art: linear-gradient(#5a5a5a, #1c1c1c); }
  .mint     { --accent: #5da68d; --art: linear-gradient(#7fae5e, #3f7a4a); }
  .teriyaki { --accent: #b7192a; --art: linear-gradient(#f6f2ee, #e4dcd6); }
  .satay    { --accent: #e9a21e; --art: linear-gradient(#f1c66a, #c98a32); }
  .bbq      { --accent: #2b2b2b; --art: linear-gradient(#3b3b3b, #6b6b6b); }
  .cajun    { --accent: #1d2a7a; --art: linear-gradient(90deg, #f2f2f2 45%, #2a3aa0 45%); }
  .buffalo  { --accent: #8a6e4a; --art: linear-gradient(#7a5a3a, #4a3220); }
  .chilli   { --accent: #7a3aa2; --art: linear-gradient(#7a2a9a, #d9461f); }
</style>
</head>
<body>
<svg width="0" height="0" style="position:absolute" aria-hidden="true">
  <defs>
    <linearGradient id="goldRim" x1="0" y1="0" x2="1" y2="1">
      <stop offset="0" stop-color="#e8d9a6"/>
      <stop offset="0.5" stop-color="#8a6a32"/>
      <stop offset="1" stop-color="#d9c48a"/>
    </linearGradient>
  </defs>
</svg>

<section class="label tomato col-1 row-1">
  <svg class="frame" viewBox="0 0 288 144" aria-hidden="true"><polygon class="outer" points="144,0 288,144 0,144"/><polygon class="accent" points="144,5 280,140 8,140"/><polygon class="inner" points="144,9 273,137 15,137"/></svg>
  <div class="art" role="img" aria-label="Illustration of a tomato with basil leaves"></div>
  <div class="brand">Tavo Crest</div>
  <div class="marinated">MARINATED WITH</div>
  <div class="name two-line">Sundried Tomato<br>&amp; Basil</div>
  <div class="spec">Please ask in store to see spec sheet for ingredients</div>
</section>

<section class="label garlic col-2 row-1">
  <svg class="frame" viewBox="0 0 288 144" aria-hidden="true"><polygon class="outer" points="144,0 288,144 0,144"/><polygon class="accent" points="144,5 280,140 8,140"/><polygon class="inner" points="144,9 273,137 15,137"/></svg>
  <div class="art" role="img" aria-label="Illustration of garlic bulbs"></div>
  <div class="brand">Tavo Crest</div>
  <div class="marinated">MARINATED WITH</div>
  <div class="name">Garlic Sprinkle</div>
  <div class="spec">Please ask in store to see spec sheet for ingredients</div>
</section>

<section class="label honey col-3 row-1">
  <svg class="frame" viewBox="0 0 288 144" aria-hidden="true"><polygon class="outer" points="144,0 288,144 0,144"/><polygon class="accent" points="144,5 280,140 8,140"/><polygon class="inner" points="144,9 273,137 15,137"/></svg>
  <div class="art" role="img" aria-label="Illustration of honeycomb"></div>
  <div class="brand">Tavo Crest</div>
  <div class="marinated">MARINATED WITH</div>
  <div class="name">Honey Soy</div>
  <div class="spec">Please ask in store to see spec sheet for ingredients</div>
</section>

<section class="label peri col-1 row-2">
  <svg class="frame" viewBox="0 0 288 144" aria-hidden="true"><polygon class="outer" points="144,0 288,144 0,144"/><polygon class="accent" points="144,5 280,140 8,140"/><polygon class="inner" points="144,9 273,137 15,137"/></svg>
  <div class="art" role="img" aria-label="Illustration of red chillies and garlic"></div>
  <div class="brand">Tavo Crest</div>
  <div class="marinated">MARINATED WITH</div>
  <div class="name">Peri Peri</div>
  <div class="spec">Please ask in store to see spec sheet for ingredients</div>
</section>

<section class="label bean col-2 row-2">
  <svg class="frame" viewBox="0 0 288 144" aria-hidden="true"><polygon class="outer" points="144,0 288,144 0,144"/><polygon class="accent" points="144,5 280,140 8,140"/><polygon class="inner" points="144,9 273,137 15,137"/></svg>
  <div class="art" role="img" aria-label="Illustration of black beans"></div>
  <div class="brand">Tavo Crest</div>
  <div class="marinated">MARINATED WITH</div>
  <div class="name">Black Bean Sauce</div>
  <div class="spec">Please ask in store to see spec sheet for ingredients</div>
</section>

<section class="label hoisin col-3 row-2">
  <svg class="frame" viewBox="0 0 288 144" aria-hidden="true"><polygon class="outer" points="144,0 288,144 0,144"/><polygon class="accent" points="144,5 280,140 8,140"/><polygon class="inner" points="144,9 273,137 15,137"/></svg>
  <div class="art" role="img" aria-label="Illustration of a red national flag"></div>
  <div class="brand">Tavo Crest</div>
  <div class="marinated">MARINATED WITH</div>
  <div class="name">Hoi-Sin Sauce</div>
  <div class="spec">Please ask in store to see spec sheet for ingredients</div>
</section>

<section class="label pepper col-1 row-3">
  <svg class="frame" viewBox="0 0 288 144" aria-hidden="true"><polygon class="outer" points="144,0 288,144 0,144"/><polygon class="accent" points="144,5 280,140 8,140"/><polygon class="inner" points="144,9 273,137 15,137"/></svg>
  <div class="art" role="img" aria-label="Illustration of black peppercorns"></div>
  <div class="brand">Tavo Crest</div>
  <div class="marinated">MARINATED WITH</div>
  <div class="name">Pepper Sprinkle</div>
  <div class="spec">Please ask in store to see spec sheet for ingredients</div>
</section>

<section class="label mint col-2 row-3">
  <svg class="frame" viewBox="0 0 288 144" aria-hidden="true"><polygon class="outer" points="144,0 288,144 0,144"/><polygon class="accent" points="144,5 280,140 8,140"/><polygon class="inner" points="144,9 273,137 15,137"/></svg>
  <div class="art" role="img" aria-label="Illustration of mint leaves and rosemary sprigs"></div>
  <div class="brand">Tavo Crest</div>
  <div class="marinated">MARINATED WITH</div>
  <div class="name">Mint &amp; Rosemary</div>
  <div class="spec">Please ask in store to see spec sheet for ingredients</div>
</section>

<section class="label teriyaki col-3 row-3">
  <svg class="frame" viewBox="0 0 288 144" aria-hidden="true"><polygon class="outer" points="144,0 288,144 0,144"/><polygon class="accent" points="144,5 280,140 8,140"/><polygon class="inner" points="144,9 273,137 15,137"/></svg>
  <div class="art" role="img" aria-label="Illustration of a white national flag with a red disc"></div>
  <div class="brand">Tavo Crest</div>
  <div class="marinated">MARINATED WITH</div>
  <div class="name">Teriyaki Sauce</div>
  <div class="spec">Please ask in store to see spec sheet for ingredients</div>
</section>

<section class="label satay col-1 row-4">
  <svg class="frame" viewBox="0 0 288 144" aria-hidden="true"><polygon class="outer" points="144,0 288,144 0,144"/><polygon class="accent" points="144,5 280,140 8,140"/><polygon class="inner" points="144,9 273,137 15,137"/></svg>
  <div class="art" role="img" aria-label="Illustration of peanuts"></div>
  <div class="brand">Tavo Crest</div>
  <div class="marinated">MARINATED WITH</div>
  <div class="name">Satay</div>
  <div class="spec">Please ask in store to see spec sheet for ingredients</div>
</section>

<section class="label bbq col-2 row-4">
  <svg class="frame" viewBox="0 0 288 144" aria-hidden="true"><polygon class="outer" points="144,0 288,144 0,144"/><polygon class="accent" points="144,5 280,140 8,140"/><polygon class="inner" points="144,9 273,137 15,137"/></svg>
  <div class="art" role="img" aria-label="Illustration of a kettle barbecue grill"></div>
  <div class="brand">Tavo Crest</div>
  <div class="marinated">MARINATED WITH</div>
  <div class="name">BBQ Sauce</div>
  <div class="spec">Please ask in store to see spec sheet for ingredients</div>
</section>

<section class="label cajun col-3 row-4">
  <svg class="frame" viewBox="0 0 288 144" aria-hidden="true"><polygon class="outer" points="144,0 288,144 0,144"/><polygon class="accent" points="144,5 280,140 8,140"/><polygon class="inner" points="144,9 273,137 15,137"/></svg>
  <div class="art" role="img" aria-label="Illustration of a regional flag in blue, white, red and gold"></div>
  <div class="brand">Tavo Crest</div>
  <div class="marinated">MARINATED WITH</div>
  <div class="name">Spicy Cajun</div>
  <div class="spec">Please ask in store to see spec sheet for ingredients</div>
</section>

<section class="label buffalo col-1 row-5">
  <svg class="frame" viewBox="0 0 288 144" aria-hidden="true"><polygon class="outer" points="144,0 288,144 0,144"/><polygon class="accent" points="144,5 280,140 8,140"/><polygon class="inner" points="144,9 273,137 15,137"/></svg>
  <div class="art" role="img" aria-label="Illustration of a buffalo head with horns"></div>
  <div class="brand">Tavo Crest</div>
  <div class="marinated">MARINATED WITH</div>
  <div class="name">Buffalo Spices</div>
  <div class="spec">Please ask in store to see spec sheet for ingredients</div>
</section>

<section class="label chilli col-2 row-5">
  <svg class="frame" viewBox="0 0 288 144" aria-hidden="true"><polygon class="outer" points="144,0 288,144 0,144"/><polygon class="accent" points="144,5 280,140 8,140"/><polygon class="inner" points="144,9 273,137 15,137"/></svg>
  <div class="art" role="img" aria-label="Illustration of plums, ginger root and a red chilli"></div>
  <div class="brand">Tavo Crest</div>
  <div class="marinated">MARINATED WITH</div>
  <div class="name two-line">Chilli, Plum<br>&amp; Ginger</div>
  <div class="spec">Please ask in store to see spec sheet for ingredients</div>
</section>
</body>
</html>
```